Redesign for Popular UK Town Website

We're looking for someone to redesign a website for a popular tourist town that's visited by over 250,000 people a year. We have a basic design frame in place and need someone to make it look more 'professional.'
We've created a temporary design layout to show you a general idea of what we're looking for: http://dorrin.co.uk/
All text/images are placeholder images so you can get an idea of the general layout.
(Please note that you can grab any images found on the internet for 'tenby' to be used as placeholder images. This is because we will be visiting the locations and taking our own photos, after the design is complete.)
Target Market(s)
Tourists
Industry/Entity Type
Town
Number of Pages Required
2 page
Requirements
Must have
- You need to redesign the homepage: http://dorrin.co.uk/
- You also need to redesign the following page: http://dorrin.co.uk/hotels/ (This page will be used for multiple categories and is used to list locations of properties/places etc.)
- Design must be responsive also.
Nice to have
- Please feel free to add as much as you can to the content/features as with our limited knowledge of websites, have only been able to create a basic layout.

```html
<!DOCTYPE html>
<html lang="en">
<head>
<meta charset="utf-8">
<title>Dorrin – Harbour Town Guide</title>
<link rel="stylesheet" href="https://fonts.googleapis.com/css2?family=Open+Sans:wght@400;600;700&display=swap">
<style>
:root{
  --blue:#1a9ae0;
  --orange:#f15a24;
  --ink:#2b2b2b;
  --text:#6d6d6d;
  --footer:#343434;
  --white:#fff;
}
*{margin:0;padding:0;box-sizing:border-box}
html,body{width:755px;height:1200px;overflow:hidden;background:var(--white)}
body{font-family:'Open Sans',sans-serif;color:var(--ink);position:relative}
.abs{position:absolute}
.hero{left:0;top:0;width:755px;height:310px;
  background:linear-gradient(180deg,#cfd3d8 0%,#c3c9cd 38%,#7f9a5e 42%,#6e8c4e 58%,#d8c9a8 62%,#b7b2a4 78%,#c9c6bd 86%,#b9bfc3 100%)}
.header{left:60px;top:14px;width:639px;height:56px;background:var(--white)}
.brand{left:12px;top:14px;display:flex;align-items:center;gap:6px}
.brand-dot{width:26px;height:26px;border-radius:50%;background:var(--blue)}
.brand-name{font-size:15px;font-weight:700;color:var(--blue);line-height:1}
.brand-tag{font-size:4px;color:var(--text);letter-spacing:.3px}
.contact{right:12px;top:16px;display:flex;gap:20px;font-size:8px;color:#555;align-items:center}
.contact span{display:flex;align-items:center;gap:5px}
.contact .phone{font-size:9px}
.nav{right:12px;top:38px;display:flex;gap:18px;font-size:7px;color:#444;letter-spacing:.2px}
.welcome{left:0;top:343px;width:755px;text-align:center}
.welcome h1{font-size:16px;font-weight:400;color:#333}
.welcome h1 b,.accent{color:var(--blue);font-weight:inherit}
.welcome p{width:590px;margin:16px auto 0;font-size:7.6px;line-height:12.4px;color:var(--text)}
.card{top:448px;width:195px;text-align:center}
.card .photo{height:96px}
.card h2{margin-top:17px;font-size:9.6px;font-weight:700;letter-spacing:.3px}
.card p{margin-top:8px;font-size:7px;line-height:9.8px;color:var(--text)}
.btn{display:inline-block;margin-top:13px;width:71px;height:24px;line-height:24px;background:var(--blue);color:var(--white);font-size:7px}
.band{left:0;top:680px;width:755px;height:245px;
  background:linear-gradient(90deg,#3e7077 0%,#33636b 55%,#e0442c 58%,#d43a26 66%,#d7d7d2 69%,#c6c8c4 84%,#3a5f64 88%,#466a6e 100%)}
.panel{left:71px;top:703px;width:359px;height:195px;background:var(--white);padding:27px 34px}
.panel h3{font-size:9.6px;font-weight:700;color:#222}
.panel .intro{margin-top:5px;font-size:7px;line-height:9.6px;color:var(--text);width:280px}
.act{font-size:8.6px;color:#555;display:flex;align-items:center;gap:8px}
.act svg{width:20px;height:18px;stroke:#666;fill:none;stroke-width:1}
.view{left:236px;top:854px;width:79px;height:26px;line-height:26px;background:var(--orange);color:var(--white);font-size:6.6px;font-weight:600;text-align:center}
.blog-title{left:0;top:948px;width:755px;text-align:center;font-size:11px;font-weight:700}
.post{top:983px;width:194px}
.post .photo{margin-top:10px;height:72px}
.date{left:9px;top:0;width:28px;height:32px;background:var(--blue);color:var(--white);text-align:center;padding-top:3px}
.date b{display:block;font-size:11px;line-height:12px}
.date small{display:block;font-size:7px;font-weight:700}
.post h4{margin-top:17px;font-size:7.6px;font-weight:700;color:#444;letter-spacing:.2px}
.post p{margin-top:5px;font-size:7px;line-height:9.8px;color:var(--text)}
.footer{left:0;top:1166px;width:755px;height:34px;background:var(--footer);color:#ccc;font-size:7.6px;text-align:center;line-height:34px}
</style>
</head>
<body>

<div class="abs hero" role="img" aria-label="Harbour town on a green headland with colourful seafront houses, a pier, a lifeboat station and a sandy beach"></div>

<header class="abs header">
  <div class="abs brand">
    <div class="brand-dot"></div>
    <div><div class="brand-name">Harbourline</div><div class="brand-tag">YOUR TAGLINE GOES HERE</div></div>
  </div>
  <div class="abs contact">
    <span><svg width="9" height="7" viewBox="0 0 9 7"><rect x=".5" y=".5" width="8" height="6" fill="none" stroke="#666"/><path d="M.5 .5 4.5 4 8.5 .5" fill="none" stroke="#666"/></svg>info@harbourline.com</span>
    <span class="phone"><svg width="8" height="8" viewBox="0 0 8 8"><path d="M1 1c0 3 3 6 6 6l.5-1.5-1.8-1-1 .8c-1-.5-1.6-1.2-2-2l.8-1-1-1.8z" fill="#666"/></svg>1020 7777 318</span>
  </div>
  <nav class="abs nav"><span>WHERE TO STAY</span><span>CARAVAN AND CAMPING</span><span>BED AND BREAKFAST</span><span>HOTELS IN DORRIN</span></nav>
</header>

<section class="abs welcome">
  <h1>Welcome to <b>DORRIN</b></h1>
  <p>The jewel in the crown of Calderwyn. A popular harbour town visited by over 299,000 visitors a year. Surrounded by its medieval stone wall, Dorrin is steeped with history and beautiful landscapes. Famed for it's beautiful beaches and views that will lure you to come back each year, we hope you enjoy your time visting and breathing in the sea air of Dorrin.</p>
</section>

<article class="abs card" style="left:70px">
  <div class="photo" role="img" aria-label="Swimmer in a wetsuit running out of the sea" style="background:linear-gradient(180deg,#b9bec0 0%,#d7d3c7 40%,#8d8f88 60%,#c9c6bd 100%)"></div>
  <h2>THINGS TO DO</h2>
  <p>The jewel in the crown of Calderwyn. A popular harbour town visited by over 299,000 visitors a year. Surrounded by its medieval stone wall,</p>
  <span class="btn">Read More</span>
</article>
<article class="abs card" style="left:281px">
  <div class="photo" role="img" aria-label="Lifeboat station with a red roof on a pier over calm water" style="background:linear-gradient(180deg,#9fb8da 0%,#a9bcd8 45%,#cfd5dc 50%,#44566a 70%,#2a3846 100%)"></div>
  <h2>PLACES TO EAT</h2>
  <p>The jewel in the crown of Calderwyn. A popular harbour town visited by over 299,000 visitors a year. Surrounded by its medieval stone wall,</p>
  <span class="btn">Read More</span>
</article>
<article class="abs card" style="left:493px">
  <div class="photo" role="img" aria-label="Colourful seafront houses above a harbour street" style="background:linear-gradient(180deg,#a9c6e2 0%,#e7c984 30%,#d9a86a 55%,#9b8b72 80%,#7a6a55 100%)"></div>
  <h2>WHERE TO STAY</h2>
  <p>The jewel in the crown of Calderwyn. A popular harbour town visited by over 299,000 visitors a year. Surrounded by its medieval stone wall,</p>
  <span class="btn">Read More</span>
</article>

<section class="abs band" role="img" aria-label="Red-roofed lifeboat station on a pier above the sea"></section>
<div class="abs panel">
  <h3>TOP 10 THINGS TO DO IN <span class="accent">DORRIN</span></h3>
  <p class="intro">With tourist flocking to Dorrin every year, there's never a shortage of things to do. This is our top 10 things to do in Dorrin and the surrounding area.</p>
  <div class="abs act" style="left:33px;top:86px"><svg viewBox="0 0 20 18"><rect x="4" y="8" width="12" height="5"/><rect x="2" y="13" width="16" height="4"/><rect x="6" y="4" width="8" height="4"/></svg>Beach Wedding</div>
  <div class="abs act" style="left:162px;top:89px"><svg viewBox="0 0 20 18"><path d="M9 2v11M9 3l7 9H9M9 5l-5 7h5M2 14h16l-2 3H4z"/></svg>Boat Trip</div>
  <div class="abs act" style="left:33px;top:117px"><svg viewBox="0 0 20 18"><path d="M10 2c3 4 4 6 4 8a4 4 0 0 1-8 0c0-2 1-4 4-8zM3 16l14-3M3 13l14 3"/></svg>Campfire</div>
  <div class="abs act" style="left:162px;top:120px"><svg viewBox="0 0 20 18"><circle cx="4.5" cy="12" r="3.5"/><circle cx="15.5" cy="12" r="3.5"/><path d="M4.5 12 8 6h6l1.5 6M8 6l3 6h-6.5M13 4h2"/></svg>Bycle</div>
  <div class="abs act" style="left:29px;top:152px"><svg viewBox="0 0 20 18"><path d="M11 1v13M11 2l4 12h-4M4 14h14M2 17h16"/></svg>Wind Surfers</div>
</div>
<div class="abs view">VIEW ALL</div>

<h2 class="abs blog-title">FROM THE BLOG</h2>

<article class="abs post" style="left:71px">
  <div class="photo" role="img" aria-label="Bandstand silhouetted against a sunset over the sea" style="background:linear-gradient(180deg,#f0b060 0%,#e59a45 45%,#a8652b 70%,#2e2218 100%)"></div>
  <div class="abs date"><b>08</b><small>DEC</small></div>
  <h4>HOTELS NEAR HOLLOW OAK WILDLIFE PARK</h4>
  <p>With tourist flocking to Dorrin every year, there's never a shortage of things to do. This is our top 10 things to do in Dorrin and the surrounding area.</p>
</article>
<article class="abs post" style="left:283px">
  <div class="photo" role="img" aria-label="Island fort on a grassy rock in the sea" style="background:linear-gradient(180deg,#8db4e0 0%,#a8c3dc 40%,#a6a852 62%,#6f7a3e 85%,#5a5a48 100%)"></div>
  <div class="abs date"><b>08</b><small>DEC</small></div>
  <h4>HOTELS NEAR HOLLOW OAK WILDLIFE PARK</h4>
  <p>With tourist flocking to Dorrin every year, there's never a shortage of things to do. This is our top 10 things to do in Dorrin and the surrounding area.</p>
</article>
<article class="abs post" style="left:495px">
  <div class="photo" role="img" aria-label="Harbour houses lit up at dusk" style="background:linear-gradient(180deg,#3a6cc0 0%,#2f5aa0 50%,#4a4c5a 70%,#7a6448 100%)"></div>
  <div class="abs date"><b>08</b><small>DEC</small></div>
  <h4>HOTELS NEAR HOLLOW OAK WILDLIFE PARK</h4>
  <p>With tourist flocking to Dorrin every year, there's never a shortage of things to do. This is our top 10 things to do in Dorrin and the surrounding area.</p>
</article>

<footer class="abs footer">Copyright Dorrin.co.uk 2017</footer>

</body>
</html>
```